Business card design needed

Can we please have exactly what I have down loaded, however change the name and cell phone/ direct line number please. Double sided thicker card and gloss please also the email address needs to be changed to PWelbourne@brightmeadowgroup.net

Industry/Entity Type

Business

Contact Information for Business Card

Paul Welbourne
Managing Director
0412 874 391
02 8173 2546

```html
<!DOCTYPE html>
<html lang="en">
<head>
<meta charset="utf-8">
<title>Business Card – Office Locations</title>
<link rel="stylesheet" href="https://fonts.googleapis.com/css2?family=Arimo:wght@400&display=swap">
<style>
  :root {
    --brand-blue: #0b7bc2;
    --brand-blue-light: #3c86c5;
    --text-white: #ffffff;
  }
  html, body {
    margin: 0;
    padding: 0;
    width: 741px;
    height: 1200px;
    overflow: hidden;
    background: var(--brand-blue);
  }
  .card-back {
    position: relative;
    width: 741px;
    height: 1200px;
    overflow: hidden;
  }
  .pattern-field {
    position: absolute;
    inset: 0;
    background: linear-gradient(160deg, var(--brand-blue-light) 0%, var(--brand-blue) 45%, var(--brand-blue-light) 100%);
  }
  .office-list {
    position: absolute;
    top: 164px;
    left: 0;
    width: 100%;
    margin: 0;
    padding: 0;
    list-style: none;
    text-align: center;
    font-family: "Arimo", Arial, sans-serif;
    font-size: 29px;
    line-height: 58.5px;
    color: var(--text-white);
  }
</style>
</head>
<body>
  <main class="card-back">
    <div class="pattern-field" role="img" aria-label="Repeating geometric pattern of light and dark blue triangles"></div>
    <ul class="office-list">
      <li>Beijing</li>
      <li>Budapest</li>
      <li>Düsseldorf</li>
      <li>London</li>
      <li>Madrid</li>
      <li>Melbourne</li>
      <li>Mexico City</li>
      <li>New York</li>
      <li>Paris</li>
      <li>Sao Paulo</li>
      <li>Seoul</li>
      <li>Sydney</li>
      <li>Toronto</li>
      <li>Tokyo</li>
      <li>Warsaw</li>
    </ul>
  </main>
</body>
</html>
```